Design a Book Cover for a Bill Tracker Logbook

We are looking for a designer to create a book cover for a bill tracker. The detailed instructions and interior pages are attached. For those who are new to RVM, the cover template is also attached.
Please be creative and focus on creating a trustworthy, reliable, modern, and secure feeling based on the theme. You are allowed to use downloaded templates, but you must provide commercial licenses.
Attention: We are happy to pay extra tip if you are selected with a really high quality design.
US

```html
<!DOCTYPE html>
<html lang="en">
<head>
<meta charset="utf-8">
<title>Bill Tracker &amp; Password Log – Cover Wrap</title>
<link rel="stylesheet" href="https://fonts.googleapis.com/css2?family=DM+Serif+Display&family=Marcellus&display=swap">
<style>
  :root {
    --cover-blue: #0057ab;
    --pocket-blue: #0679bf;
    --pocket-rim: #004a96;
    --line-blue: #6fb0e0;
    --ink-light: #f3f6fb;
    --ink-soft: #e4ecf7;
    --paper-light: #f1f4f8;
    --paper-shade: #d9dee5;
    --seal-dark: #1b2433;
    --date-box: #c9dcf0;
    --barcode-box: #e8eff8;
  }
  * { margin: 0; padding: 0; box-sizing: border-box; }
  html, body { width: 1200px; height: 772px; overflow: hidden; background: var(--cover-blue); }
  .cover-wrap { position: relative; width: 1200px; height: 772px; background: var(--cover-blue); overflow: hidden; }
  .artwork { position: absolute; inset: 0; }

  .publisher-mark {
    position: absolute; left: 236px; top: 174px; display: flex; align-items: center; gap: 8px;
    font-family: "Marcellus", serif; font-size: 13px; line-height: 22px; color: var(--ink-light); letter-spacing: 0.5px;
  }
  .publisher-mark .seal { width: 22px; height: 22px; border-radius: 50%; background: var(--seal-dark); }

  .back-note {
    position: absolute; left: 20px; top: 240px; width: 560px; text-align: center; white-space: nowrap;
    font-family: "Marcellus", serif; font-size: 18px; line-height: 25px; color: var(--ink-light);
  }
  .barcode-space { position: absolute; left: 437px; top: 664px; width: 137px; height: 82px; background: var(--barcode-box); }

  .spine-title {
    position: absolute; left: 592px; top: 113px; writing-mode: vertical-rl;
    font-family: "Marcellus", serif; font-size: 6.5px; letter-spacing: 0.1px; color: var(--ink-light);
  }

  .feature-list { position: absolute; left: 676px; font-family: "Marcellus", serif; font-size: 21px; line-height: 21px; color: var(--ink-soft); }
  .feature-list.passwords { top: 628px; }
  .feature-list.payments { top: 680px; }

  .page-count {
    position: absolute; left: 930px; top: 630px; width: 230px; text-align: center;
    font-family: "Marcellus", serif; font-size: 36px; line-height: 40px; color: var(--ink-light);
  }
  .date-range {
    position: absolute; left: 933px; top: 672px; width: 225px; height: 38px; background: var(--date-box);
    font-family: "Marcellus", serif; font-size: 22px; line-height: 38px; color: var(--cover-blue); padding-left: 12px; white-space: nowrap;
  }
  .date-range .blank { display: inline-block; width: 28px; border-bottom: 1.5px solid var(--cover-blue); height: 1px; vertical-align: 4px; margin-right: 4px; }
</style>
</head>
<body>
<main class="cover-wrap">
  <svg class="artwork" width="1200" height="772" viewBox="0 0 1200 772" xmlns="http://www.w3.org/2000/svg">
    <defs>
      <linearGradient id="sheetTone" x1="0" y1="0" x2="0" y2="1">
        <stop offset="0" stop-color="var(--paper-light)"/>
        <stop offset="1" stop-color="var(--paper-shade)"/>
      </linearGradient>
    </defs>

    <polygon class="back-flap" points="0,0 589,0 299,170" fill="var(--pocket-blue)"/>

    <g class="cover-title" fill="#ffffff" font-family="DM Serif Display, serif">
      <text x="705" y="211" font-size="196" textLength="390" lengthAdjust="spacingAndGlyphs">BILL</text>
      <text x="706" y="300" font-size="90" textLength="388" lengthAdjust="spacingAndGlyphs">TRACKER</text>
      <text x="708" y="358" font-size="49" textLength="386" lengthAdjust="spacingAndGlyphs">&amp; PASSWORD LOG</text>
    </g>

    <polygon class="interior-preview" role="img"
      aria-label="Fanned interior page samples: password log, bill tracker and contacts sheets"
      points="665,428 806,412 806,395 1038,395 1038,404 1150,455 900,600 680,470"
      fill="url(#sheetTone)"/>

    <polygon class="pocket-rim" points="608,421 900,594 1200,421 1200,426 900,600 608,428" fill="var(--pocket-rim)"/>
    <polygon class="pocket" points="608,426 900,599 1200,426 1200,772 608,772" fill="var(--pocket-blue)"/>
    <g class="pocket-stitch" stroke="var(--line-blue)" stroke-width="0.8" fill="none">
      <polyline points="628,457 900,618 1186,457"/>
      <line x1="900" y1="618" x2="900" y2="747"/>
    </g>
  </svg>

  <div class="publisher-mark"><span class="seal"></span><span class="name">Owen Halvard</span></div>

  <p class="back-note">Thank you for choosing “Bill Tracker &amp; Password Log”,<br>please leave a review on Pagewell if you find it helpful in your<br>life, this will help us produce more high-quality content.<br>Thank you.</p>

  <div class="barcode-space"></div>

  <div class="spine-title">BILL TRACKER &amp; PASSWORD LOG</div>

  <p class="feature-list passwords">Save Passwords<br>and Contacts</p>
  <p class="feature-list payments">Track Payments<br>up to 8 Years</p>

  <p class="page-count">100 + Pages</p>
  <p class="date-range">From 20<span class="blank"></span>to 20<span class="blank"></span></p>
</main>
</body>
</html>
```